Computer tuition business needs Business card and Advertising Flyer

I am starting up a new business "Dorian Featherby Computer Services" (DFCS for short) based in the Manning Valley NSW Australia.
The primary focus is on tuition\advice to the elderly and less computer literate in the region.
I will not be providing any repair services.

I have the line "At your home, On your computer, Answering your questions" in my head

I will need a Business card design (one sided) and Advertising Flyer design (A4 size, grayscale ).

Contact details on all these are - Mobile: 0412-683-904
- Email : dfeatherby.techhelp@examplemail.net

Target Market(s)

The primary focus is on tuition\advice to the elderly and less computer literate in the Manning Valley region of

Industry/Entity Type

Computer

```html
<!DOCTYPE html>
<html lang="en">
<head>
<meta charset="utf-8">
<title>Dorian Featherby Computer Services – Flyer</title>
<link rel="stylesheet" href="https://fonts.googleapis.com/css2?family=Open+Sans:wght@400;600;700;800&display=swap">
<style>
  :root {
    --stage: #2a2a2a;
    --paper: #ffffff;
    --band: #6e6e6e;
    --ink: #5e5e5e;
    --ink-strong: #646464;
    --frame: #707070;
    --bubble: #6a6a6a;
    --on-band: #ffffff;
    --photo-light: #f1f1f1;
    --photo-mid: #bdbdbd;
  }
  * { box-sizing: border-box; margin: 0; padding: 0; }
  html, body { width: 1200px; height: 800px; overflow: hidden; }
  body {
    background: var(--stage);
    font-family: "Open Sans", sans-serif;
    display: flex;
    align-items: center;
    justify-content: center;
  }
  .flyer {
    position: relative;
    width: 560px;
    height: 792px;
    background: var(--paper);
    overflow: hidden;
  }
  .tagline-band {
    position: absolute;
    top: 0; left: 0; right: 0;
    height: 44px;
    background: var(--band);
    color: var(--on-band);
    font-weight: 700;
    font-size: 17px;
    display: flex;
    align-items: center;
    justify-content: center;
    letter-spacing: 0.1px;
  }
  .hero-photo {
    position: absolute;
    left: 150px; top: 150px;
    width: 320px; height: 250px;
    background: radial-gradient(ellipse at 55% 40%, var(--photo-mid) 0%, #d8d8d8 45%, var(--photo-light) 75%, var(--paper) 100%);
  }
  .thoughts { position: absolute; inset: 0; pointer-events: none; }
  .bubble-text {
    font-family: "Open Sans", sans-serif;
    font-weight: 700;
    fill: var(--on-band);
    font-size: 11px;
  }
  .question-mark {
    font-family: "Open Sans", sans-serif;
    font-weight: 700;
    fill: var(--ink);
    font-size: 46px;
  }
  .offer-box {
    position: absolute;
    left: 50px; top: 356px;
    width: 460px;
    border: 5px solid var(--frame);
    border-radius: 18px;
    background: rgba(255,255,255,0.92);
    padding: 16px 22px 22px 22px;
  }
  .offer-list { list-style: none; }
  .offer-list li {
    position: relative;
    padding-left: 26px;
    color: var(--ink);
    font-size: 16px;
    line-height: 1.32;
  }
  .offer-list li svg {
    position: absolute;
    left: 2px; top: 6px;
    width: 13px; height: 11px;
  }
  .business-name {
    margin-top: 22px;
    margin-left: 6px;
    color: var(--ink-strong);
    font-weight: 800;
    font-size: 38px;
    line-height: 1.05;
    letter-spacing: -0.4px;
    white-space: nowrap;
  }
  .business-type {
    margin-top: 4px;
    margin-left: 10px;
    color: var(--ink-strong);
    font-weight: 700;
    font-size: 22px;
    line-height: 1.2;
  }
  .contact-band {
    position: absolute;
    left: 0; right: 0; bottom: 0;
    height: 104px;
    background: var(--band);
    color: var(--on-band);
    font-weight: 700;
    font-size: 17px;
    padding: 16px 22px;
  }
  .contact-email { display: block; }
  .contact-phone {
    position: absolute;
    right: 22px; bottom: 18px;
    font-size: 21px;
  }
</style>
</head>
<body>
  <main class="flyer">
    <header class="tagline-band">At your home, On your computer, Answering your questions</header>

    <div class="hero-photo" role="img" aria-label="Photo of a puzzled man in shirt and tie sitting at a laptop, chin resting on his hand"></div>

    <svg class="thoughts" viewBox="0 0 560 792">
      <g class="thought-left">
        <ellipse cx="112" cy="98" rx="72" ry="36" fill="var(--bubble)"/>
        <circle cx="168" cy="146" r="8" fill="var(--bubble)"/>
        <circle cx="186" cy="162" r="6" fill="var(--bubble)"/>
        <circle cx="200" cy="174" r="4" fill="var(--bubble)"/>
        <text class="bubble-text" x="112" y="94" text-anchor="middle">Wish I had</text>
        <text class="bubble-text" x="112" y="108" text-anchor="middle">learned computer...</text>
      </g>
      <text class="question-mark" x="268" y="150" text-anchor="middle">?</text>
      <g class="thought-right">
        <ellipse cx="460" cy="230" rx="62" ry="32" fill="var(--bubble)"/>
        <circle cx="392" cy="246" r="7" fill="var(--bubble)"/>
        <circle cx="376" cy="252" r="5" fill="var(--bubble)"/>
        <circle cx="364" cy="256" r="3.5" fill="var(--bubble)"/>
        <text class="bubble-text" x="460" y="226" text-anchor="middle">But Where</text>
        <text class="bubble-text" x="460" y="241" text-anchor="middle">Do I STAR?</text>
      </g>
    </svg>

    <section class="offer-box">
      <ul class="offer-list">
        <li><svg viewBox="0 0 13 11"><path d="M1 6 L5 9.5 L12 1.5" fill="none" stroke="var(--ink)" stroke-width="2"/></svg>Computer lessons for new beginners</li>
        <li><svg viewBox="0 0 13 11"><path d="M1 6 L5 9.5 L12 1.5" fill="none" stroke="var(--ink)" stroke-width="2"/></svg>Initial set up and overview</li>
        <li><svg viewBox="0 0 13 11"><path d="M1 6 L5 9.5 L12 1.5" fill="none" stroke="var(--ink)" stroke-width="2"/></svg>Lessons per hour in the comfort of your own home</li>
        <li><svg viewBox="0 0 13 11"><path d="M1 6 L5 9.5 L12 1.5" fill="none" stroke="var(--ink)" stroke-width="2"/></svg>A learning and training plan presented based on your requirements</li>
        <li><svg viewBox="0 0 13 11"><path d="M1 6 L5 9.5 L12 1.5" fill="none" stroke="var(--ink)" stroke-width="2"/></svg>An appraisal update on your new skills</li>
      </ul>
      <h1 class="business-name">Dorian Featherby</h1>
      <p class="business-type">Computer Services</p>
    </section>

    <footer class="contact-band">
      <span class="contact-email">Email:&nbsp; dfeatherby.techhelp@examplemail.net</span>
      <span class="contact-phone">Ph: 0412-683-904</span>
    </footer>
  </main>
</body>
</html>
```